Printed magazine advertisement for a book about piano styles.

Hello all,

I need a design for an ad:

Goal: I am trying to promote my book about various national styles of playing classical piano.

1. Ad will be printed in several piano-related magazines, here are examples:

http://www.brambleworth.co.uk/brambleworth-press/journals/tessaly-review/
http://www.klvb.org/
https://www.corvelmonthly.com/

2. I would like to ask for a design that can be adjusted to 3 size specifications so that I can post it in magazines (please see 'File specifications' attachment).

3. To save you time, please create a design in a single format. If successful, we can then adjust it to other specifications.

4. Here is my website this discusses the book: http://veldmarkhollowayinc.com/

5. If possible, the design should include:
- QRS code
- Zubrix logo (book is available through Zubrix, please pick logo version suitable to your design)
- Book cover (it can include only the front page, up to your discretion)
- Blurb (see 'Ad blurb')

7. The character of the ad should be: classy, trustworthy, professional

Please let me know if there are any issues with fitting all the required text into the specified size. I can try to make it shorter.

Thank you for your interest.

Target Market(s)

Piano professionals, pianists, teachers, academic researchers

Requirements
Must have
• All must haves are already described in Project description.

```html
<!DOCTYPE html>
<html lang="en">
<head>
<meta charset="utf-8">
<title>Charting Regional Piano Lineages – Advertisement</title>
<link rel="stylesheet" href="https://fonts.googleapis.com/css2?family=Cinzel:wght@400;500&family=Della+Respira&display=swap">
<style>
  :root {
    --page: #ffffff;
    --panel-dark: #0f1212;
    --panel-mid: #3a3c3d;
    --ink: #f4f4f2;
    --accent: #e0921f;
    --frame: #e8e8e6;
    --cover-blue: #5f7890;
    --cover-dark: #1b1c1f;
  }
  * { margin: 0; padding: 0; box-sizing: border-box; }
  html, body {
    width: 1200px; height: 1200px; overflow: hidden;
    background: var(--page);
  }
  .canvas { position: relative; width: 1200px; height: 1200px; }
  .ad-panel {
    position: absolute; left: 39px; top: 199px; width: 1122px; height: 801px;
    overflow: hidden;
    background:
      radial-gradient(ellipse 520px 260px at 380px 10px, rgba(200,200,200,0.85), rgba(120,120,120,0.35) 55%, transparent 80%),
      radial-gradient(ellipse 380px 600px at 80px 500px, rgba(170,170,170,0.55), transparent 70%),
      linear-gradient(180deg, var(--panel-mid) 0%, #1c1e1f 45%, var(--panel-dark) 100%);
  }
  .body-text {
    font-family: "Della Respira", Georgia, serif;
    color: var(--ink);
    font-size: 24px;
    line-height: 29px;
    letter-spacing: 0.3px;
    text-align: justify;
    text-align-last: left;
  }
  .blurb { position: absolute; left: 203px; top: 76px; width: 714px; }
  .title-frame {
    position: absolute; left: 207px; top: 293px; width: 710px; height: 215px;
    border: 2px solid var(--frame);
    text-align: center; color: var(--ink);
    font-family: "Cinzel", "Times New Roman", serif;
  }
  .title-top { font-size: 44px; margin-top: 26px; line-height: 48px; letter-spacing: 0.5px; }
  .title-main { font-size: 74px; line-height: 78px; letter-spacing: 0.5px; white-space: nowrap; }
  .title-sub {
    font-family: "Della Respira", Georgia, serif;
    font-size: 24px; margin-top: 6px;
  }
  .quote { position: absolute; left: 203px; top: 558px; width: 660px; }
  .website {
    position: absolute; left: 207px; top: 716px;
    font-family: "Della Respira", Georgia, serif;
    font-size: 24px; color: var(--accent);
  }
  .retailer {
    position: absolute; left: 759px; top: 705px; color: var(--ink);
    font-family: "Della Respira", Georgia, serif;
  }
  .retailer-label { font-size: 12px; }
  .retailer-name { font-size: 30px; line-height: 32px; }
  .book-cover {
    position: absolute; left: 891px; top: 461px; width: 194px; height: 300px;
    background: linear-gradient(180deg, var(--cover-blue) 0%, #3a4b5c 45%, var(--cover-dark) 60%, var(--cover-dark) 100%);
    box-shadow: 4px 4px 10px rgba(0,0,0,0.6);
    transform: skewY(-3deg);
  }
</style>
</head>
<body>
<div class="canvas">
  <section class="ad-panel" role="img" aria-label="Dark black-and-white photograph of a grand piano keyboard and curved lid">
    <p class="body-text blurb">This book is the result of a six-year doctoral investigation into the phenomenon of ‘national piano schools’. It describes the current state and evolution of Russian, Austro-German and French piano styles amongst others, and identifies key areas through which the schools may be defined (such as history, language, technique, and cultural heritage).</p>

    <div class="title-frame">
      <div class="title-top">Charting Regional</div>
      <div class="title-main">Piano Lineages</div>
      <div class="title-sub">Heritage and challenges - Dr Tomasz Kelvarin</div>
    </div>

    <p class="body-text quote">“Pianists often trace their lineage back to, for example, Haldorff. But I think through changes in society, migration of the people, the whole change of attitude, I do not think there is anything left of that Haldorff tradition.”<br>(Interview 4) (Chapter 6)</p>

    <div class="website">www.veldmarkhollowayinc.com</div>

    <div class="retailer">
      <div class="retailer-label">Available at</div>
      <div class="retailer-name">Zubrix</div>
    </div>

    <div class="book-cover" role="img" aria-label="Front cover of the book Charting Regional Piano Lineages by Tomasz Kelvarin"></div>
  </section>
</div>
</body>
</html>
```